Business Card Design Project

I would like a business card created for a new company. This is a holding company that acts as my investment company. It holds real estate and service based companies. The name of the company is Sandorecca which is Italian for Evolution. Defined as development or growth.
We currently have no logo. I really like some of the "different" cards out there. Potentially metallic or grey/black. That looks premium/hi-end and unique. I am not sure if your design would be specific to the card stock I end with our just logo/design/font.
Real Estate

```html
<!DOCTYPE html>
<html lang="en">
<head>
<meta charset="utf-8">
<title>Sandorecca — Business Card</title>
<link rel="stylesheet" href="https://fonts.googleapis.com/css2?family=Orbitron:wght@700&family=Arimo&display=swap">
<style>
  :root {
    --card-base: #3d5356;
    --card-glow: #5b7275;
    --card-deep: #26363a;
    --band-top: #5d7274;
    --band-top-edge: #8a9d9e;
    --band-bottom: #4b6366;
    --band-bottom-edge: #6f8587;
    --wordmark: #1c282b;
    --tagline: #d4dddd;
  }
  html, body {
    margin: 0;
    padding: 0;
    width: 1200px;
    height: 621px;
    overflow: hidden;
    background: var(--card-deep);
  }
  .card {
    position: relative;
    width: 1200px;
    height: 621px;
    overflow: hidden;
    background:
      radial-gradient(ellipse 60% 55% at 45% 55%, var(--card-glow) 0%, var(--card-base) 55%, var(--card-deep) 100%);
  }
  .band-top {
    position: absolute;
    left: 0; top: 0;
    width: 100%;
    height: 62px;
    background: linear-gradient(180deg, var(--band-top-edge) 0%, var(--band-top) 30%, var(--card-base) 100%);
    opacity: 0.85;
  }
  .band-bottom {
    position: absolute;
    left: 0; bottom: 0;
    width: 100%;
    height: 134px;
    background: linear-gradient(180deg, var(--band-bottom-edge) 0%, var(--band-bottom) 12%, var(--card-base) 100%);
    opacity: 0.9;
  }
  .wordmark {
    position: absolute;
    left: 0; top: 0;
    width: 1200px;
    height: 621px;
  }
  .wordmark text {
    font-family: "Orbitron", "Arial Black", sans-serif;
    font-weight: 700;
    fill: var(--wordmark);
  }
  .tagline {
    position: absolute;
    top: 504px;
    margin: 0;
    font-family: "Arimo", Arial, sans-serif;
    font-size: 44px;
    line-height: 1;
    color: var(--tagline);
    white-space: nowrap;
  }
  .tagline-left { left: 76px; }
  .tagline-right { left: 758px; }
</style>
</head>
<body>
  <div class="card">
    <div class="band-top"></div>
    <div class="band-bottom"></div>
    <svg class="wordmark" viewBox="0 0 1200 621" aria-label="Sandorecca">
      <text x="68" y="377" font-size="200" textLength="1076" lengthAdjust="spacingAndGlyphs">Sandorecca</text>
    </svg>
    <p class="tagline tagline-left">Lorem ipsum dolor sit amet</p>
    <p class="tagline tagline-right">ipsum dolor sit amet</p>
  </div>
</body>
</html>
```